business card design

i would like business cards designed. My business provides trade qualified personnel to the mining industry to work on heavy mobile equipment.
please put a excavator(digger) in the background in one design and have one design without so i can compare the difference.
also add info:
my logo(attached) and "mobile equipment repair and maintenance"
name: Derek Holloway
address: 57 Tarrowby RD Carmel Perth WA.
mobile: 0438120957
email: derek@ironvalemx.com

```html
<!DOCTYPE html>
<html lang="en">
<head>
<meta charset="utf-8">
<title>Ironvale Maintenance Services – Business Cards</title>
<link href="https://fonts.googleapis.com/css2?family=Poppins:wght@400;500;700&display=swap" rel="stylesheet">
<style>
  :root {
    --navy: #021f41;
    --navy-soft: #0b2a4d;
    --white: #ffffff;
    --ghost: #ebebeb;
    --stage: #f1f1f1;
    --ink: #0a1c35;
  }
  * { box-sizing: border-box; margin: 0; padding: 0; }
  html, body {
    width: 1200px; height: 1200px; overflow: hidden;
    background: var(--stage);
    font-family: "Poppins", sans-serif;
  }
  .sheet { position: relative; width: 1200px; height: 1200px; }
  .card {
    position: absolute; top: 464px;
    width: 403px; height: 269px; overflow: hidden;
  }
  .card--front { left: 173px; background: var(--navy); }
  .card--back  { left: 623px; background: var(--white); }

  .machine-art { position: absolute; }
  .card--front .machine-art {
    left: 159px; top: 89px; width: 244px; height: 180px;
    background: radial-gradient(ellipse at 60% 55%, var(--navy-soft) 0%, rgba(11,42,77,0.5) 60%, rgba(2,31,65,0) 100%);
  }
  .card--back .machine-art {
    left: 153px; top: 89px; width: 250px; height: 162px;
    background: radial-gradient(ellipse at 55% 55%, var(--ghost) 0%, rgba(235,235,235,0.6) 60%, rgba(255,255,255,0) 100%);
  }

  .brand-block {
    position: absolute; left: 0; right: 0; top: 86px;
    text-align: center; color: var(--white);
  }
  .brand-name {
    font-weight: 700; font-size: 25px; line-height: 26px;
    letter-spacing: 2px;
  }
  .brand-sub {
    font-weight: 500; font-size: 6.8px; letter-spacing: 1.2px;
    margin-top: 3px;
  }
  .tagline {
    position: absolute; left: 114px; width: 175px; top: 150px; height: 23px;
    border-top: 1px solid var(--white); border-bottom: 1px solid var(--white);
    color: var(--white); font-size: 6.6px; font-weight: 500;
    display: flex; align-items: center; justify-content: center;
    letter-spacing: 0.1px;
  }

  .holder-name {
    position: absolute; left: 38px; top: 36px;
    font-weight: 700; font-size: 19px; color: var(--navy);
  }
  .contact {
    position: absolute; left: 38px; top: 174px;
    border-left: 3px solid var(--navy); padding-left: 6px;
    color: var(--ink); font-size: 9.6px; line-height: 19.5px;
    list-style: none; height: 50px;
  }
  .contact li { line-height: 19.5px; margin-top: -4px; }
  .contact li + li { margin-top: 0; }
  .brand-mini {
    position: absolute; left: 285px; top: 208px; width: 80px;
    text-align: center; color: var(--navy);
  }
  .brand-mini .brand-name { font-size: 11px; line-height: 12px; letter-spacing: 1px; }
  .brand-mini .brand-sub { font-size: 3.2px; letter-spacing: 0.4px; margin-top: 1px; }
  .base-band {
    position: absolute; left: 0; bottom: 0; width: 100%; height: 17px;
    background: var(--navy);
  }
</style>
</head>
<body>
<main class="sheet">
  <section class="card card--front">
    <div class="machine-art" role="img" aria-label="Faint excavator silhouette in the background"></div>
    <div class="brand-block">
      <div class="brand-name">IRONVALE</div>
      <div class="brand-sub">MAINTENANCE SERVICES PTY LTD</div>
    </div>
    <div class="tagline">MOBILE EQUIPMENT REPAIR AND MAINTENANCE</div>
  </section>

  <section class="card card--back">
    <div class="machine-art" role="img" aria-label="Light grey excavator silhouette in the background"></div>
    <h1 class="holder-name">Derek Holloway</h1>
    <ul class="contact">
      <li>0438120957</li>
      <li>57 Tarrowby RD Carmel Perth WA.</li>
      <li>derek@ironvalemx.com</li>
    </ul>
    <div class="brand-mini">
      <div class="brand-name">IRONVALE</div>
      <div class="brand-sub">MAINTENANCE SERVICES PTY LTD</div>
    </div>
    <div class="base-band"></div>
  </section>
</main>
</body>
</html>
```